Communication Business Card Design

We offer complete cabling solutions
Data Cabling,Fibre Optic, and Cabling Repairs fault finding
Security camera installation
TV Aerial installation
Security alarm installation
HWR

Industry/Entity Type

Business

Contact Information for Business Card

Brightmoor Solutions
ABN 58 214 992 367
EMAIL brightmoorsolutions.com.au
Mobile 0491236057
Lou Archer

```html
<!DOCTYPE html>
<html lang="en">
<head>
<meta charset="utf-8">
<title>Brightmoor Solutions – Business Card</title>
<link rel="stylesheet" href="https://fonts.googleapis.com/css2?family=Questrial&display=swap">
<style>
  :root {
    --stage: #1c1c1c;
    --card: #05060f;
    --card-deep: #0a0d26;
    --accent: #1a9fe0;
    --ink: #e9eef5;
  }
  * { box-sizing: border-box; margin: 0; padding: 0; }
  html, body {
    width: 1200px; height: 1067px; overflow: hidden;
    background: var(--stage);
    font-family: "Questrial", "Century Gothic", sans-serif;
  }
  .card {
    position: absolute; left: 160px; width: 880px; height: 500px;
    background: radial-gradient(ellipse at 70% 20%, var(--card-deep), var(--card) 70%);
    overflow: hidden; border-radius: 4px;
    box-shadow: 0 10px 30px rgba(0,0,0,.5);
  }
  .card--back { top: 22px; }
  .card--front { top: 545px; }

  .cable-art {
    position: absolute;
    background:
      radial-gradient(ellipse at 60% 55%, rgba(27,79,214,.75), transparent 45%),
      radial-gradient(ellipse at 80% 40%, rgba(154,162,173,.55), transparent 40%),
      radial-gradient(ellipse at 30% 70%, rgba(47,127,216,.45), transparent 50%),
      linear-gradient(160deg, #0a0d26 0%, #111a3d 50%, #1d2540 100%);
  }
  .card--back .cable-art { left: 0; top: 250px; width: 880px; height: 250px; }
  .card--front .cable-art { left: 440px; top: 170px; width: 440px; height: 330px; border-top-left-radius: 60% 40%; }

  /* back side */
  .offer {
    position: absolute; left: 0; top: 48px; width: 880px; text-align: center;
    color: var(--ink); font-size: 25px; line-height: 46px;
  }
  .offer__title {
    color: var(--accent); font-size: 25px;
    text-decoration: underline; text-underline-offset: 4px;
    margin-bottom: 8px; line-height: 34px;
  }
  .offer__sep {
    display: inline-block; width: 16px; height: 16px; margin: 0 14px;
    border: 4px solid var(--accent); border-radius: 50%; vertical-align: -1px;
  }

  /* front side */
  .brand {
    position: absolute; right: 50px; top: 70px;
    color: var(--accent); font-size: 38px; line-height: 44px;
  }

  .contact {
    position: absolute; left: 40px; top: 190px; width: 440px; text-align: right;
    color: var(--ink); font-size: 24px; line-height: 32px;
  }
  .contact__name { color: var(--accent); font-size: 25px; margin-bottom: 6px; }
  .contact__label { color: var(--accent); }
</style>
</head>
<body>

<section class="card card--back" aria-label="Business card back">
  <div class="cable-art" role="img" aria-label="Close-up illustration of a fibre optic cable with coloured inner tubes and glowing blue light strands"></div>
  <div class="offer">
    <p class="offer__title">WE OFFER</p>
    <p>Data Cabling<span class="offer__sep"></span>Fibre Optic Cabling Repairs fault finding</p>
    <p>Security camera installation<span class="offer__sep"></span>TV Aerial installation</p>
    <p>Security alarm installation<span class="offer__sep"></span>HWR</p>
  </div>
</section>

<section class="card card--front" aria-label="Business card front">
  <div class="cable-art" role="img" aria-label="Illustration of a fibre optic cable end with red, green, yellow and blue tubes and glowing light strands"></div>
  <p class="brand">Brightmoor Solutions</p>
  <div class="contact">
    <p class="contact__name">LOU ARCHER</p>
    <p><span class="contact__label">Phone:</span> 049 123 6057</p>
    <p><span class="contact__label">Mail:</span> info@brightmoorsolutions.com.au</p>
    <p><span class="contact__label">Web:</span> www.brightmoorsolutions.com.au</p>
    <p><span class="contact__label">ABN</span> 58 214 992 367</p>
  </div>
</section>

</body>
</html>
```